Label Redesign For Hemp Oil Tincture Bottle*

I need a label redesigned for Marbleleaf Hemp, current bottle label and logo is attached. The current label doesn't standout, not sure if its the font size or colors on the existing label. It is very important to have on the label that this is a Premium Full Spectrum Hemp Oil that is 2000mg. Then after the label is redesigned and approved, I would need to packaging to be designed to match the approved label design.
This Hemp oil has a relaxing effect to help ease mental and emotional stress, tension and worry. The Omega Fatty Acids it contains also naturally improves your mood and overall brain function, causing you to feel more alert and focused. Hemp Oil helps with insomnia. Take some 2-3 hours before bedtime, you will feel relaxed yet aware of how tired you are that it will lead to a good night's sleep. Hemp Oil helps ease chronic pain and inflammation from conditions such as arthritis, fibromyalgia, lupus, and MS. As a pain relief supplement, it is a safer, natural, non-chemical and non-addictive alternative to prescription painkillers.

Target Market(s)

Adults

Industry/Entity Type

Supplement

Font styles to use
Serif
Sans Serif

Colors

Designer to choose colors to be used in the design.

Requirements
Must have
• All information thats on current label but where it says 750 in the front of the existing label, it needs to say 2000. The 2000 should be prominent on the label.

```html
<!DOCTYPE html>
<html lang="en">
<head>
<meta charset="utf-8">
<title>Marbleleaf Hemp – Tincture Label</title>
<link href="https://fonts.googleapis.com/css2?family=Tinos:wght@400;700&family=Barlow+Semi+Condensed:wght@400;500;600&display=swap" rel="stylesheet">
<style>
  :root{
    --stripe-red:#b3191f;
    --stripe-dark:#3b0a0b;
    --center-dark:#2a0c0c;
    --center-green:#1f3a1c;
    --panel-tan:#d6b274;
    --panel-light:#fffdf8;
    --ink:#111111;
    --rule:#2a2a2a;
    --white:#ffffff;
    --seal-green:#1e4a26;
    --seal-light:#f4f1dc;
    --seal-edge:#c9c290;
    --mark:#9cc14d;
  }
  *{margin:0;padding:0;box-sizing:border-box}
  html,body{width:1200px;height:657px;overflow:hidden;background:#fff}
  .label{
    position:relative;width:1200px;height:657px;overflow:hidden;
    background:repeating-linear-gradient(180deg,var(--stripe-red) 0 3px,var(--stripe-dark) 3px 6px);
    font-family:"Tinos",serif;color:var(--ink);
  }
  .front{
    position:absolute;left:365px;top:0;width:468px;height:657px;
    background:
      linear-gradient(90deg,rgba(60,10,10,0) 0,rgba(25,8,8,.85) 18%,rgba(25,8,8,.9) 82%,rgba(60,10,10,0) 100%),
      repeating-linear-gradient(180deg,var(--center-green) 0 3px,var(--center-dark) 3px 6px);
  }
  .panel{
    position:absolute;top:47px;height:561px;border-radius:28px;
    background:linear-gradient(180deg,var(--panel-tan) 0%,var(--panel-light) 50%,var(--panel-tan) 100%);
  }
  .panel--use{left:47px;width:317px}
  .panel--facts{left:833px;width:314px}

  .directions{position:absolute;left:13px;top:46px;width:290px;font-size:14px;line-height:20px}
  .directions p{margin-bottom:18px}
  .directions b{font-weight:700}

  .brand-mark{position:absolute;left:571px;top:48px;width:52px;height:52px;border-radius:50%;background:var(--mark)}
  .brand-name{position:absolute;left:0;right:0;top:160px;text-align:center;font-weight:700;font-size:38px;color:var(--white)}
  .front-inner{position:absolute;left:0;top:0;width:1200px;height:657px;pointer-events:none}

  .seal{
    position:absolute;left:483px;top:206px;width:228px;height:228px;border-radius:50%;
    background:radial-gradient(circle at 50% 45%,var(--seal-light) 0 55%,var(--seal-edge) 100%);
    text-align:center;color:var(--seal-green);font-weight:700;
  }
  .seal-plant{
    position:absolute;left:64px;top:14px;width:100px;height:88px;border-radius:50% 50% 40% 40%;
    background:radial-gradient(ellipse at 50% 40%,#6f8a4e 0,#a9b98a 60%,rgba(244,241,220,0) 100%);
  }
  .seal-text{position:absolute;left:0;right:0;top:100px;font-size:22px;line-height:29px}

  .strength{position:absolute;left:0;right:0;top:448px;text-align:center;color:var(--white)}
  .strength-amount{font-size:46px;font-weight:700;line-height:56px;display:block;margin-left:-6px}
  .strength-type{font-size:16.5px;font-weight:700;line-height:22px;display:block;margin-top:4px}
  .flavor{position:absolute;left:0;right:0;top:578px;text-align:center;color:var(--white);font-size:19px;font-weight:700}

  .facts{
    position:absolute;left:16px;top:26px;width:282px;border:2.5px solid var(--rule);
    font-family:"Barlow Semi Condensed",sans-serif;font-size:14px;line-height:18px;
  }
  .facts-row{padding:0 12px;border-top:2.5px solid var(--rule);display:flex;align-items:center;justify-content:space-between}
  .facts-row:first-child{border-top:none}
  .facts-head{display:block;padding-top:12px;height:82px}
  .facts-head strong{font-weight:600;display:block}
  .facts-calories{height:32px;font-weight:600}
  .facts-fat{height:35px;font-weight:600}
  .facts-extract{height:39px}
  .facts-other{display:block;height:48px;padding-top:5px}
  .distributor{position:absolute;left:18px;top:308px;font-size:13px;line-height:18px;font-weight:700}
</style>
</head>
<body>
<div class="label">
  <div class="front"></div>

  <section class="panel panel--use">
    <div class="directions">
      <p><b>SUGESTED USE:</b><br>Shake well before each use. Take 30 drops (1 full dropper) and place in mouth underneath tongue for 90 seconds 2-1 times daily or as recommended by a Physician.</p>
      <p><b>WARNINGS:</b> If you are prenant or breastfeeding, consult a health care practitioner before using.</p>
      <p><b>KEEP OUT OF REACH<br>OF CHILDREN</b></p>
      <p><b>DO NOT USE IF SEAL<br>IS BROKEN OR<br>MISSING</b></p>
    </div>
  </section>

  <div class="front-inner">
    <div class="brand-mark"></div>
    <h1 class="brand-name">Marbleleaf Hemp</h1>
    <div class="seal">
      <div class="seal-plant" role="img" aria-label="Illustration of a hemp plant"></div>
      <div class="seal-text">Premium<br>Full Spectrum<br>2000<br>Hemp Oil</div>
    </div>
    <div class="strength">
      <span class="strength-amount">2000 mg</span>
      <span class="strength-type">DIETARY SUPPLEMENT</span>
      <span class="strength-type" style="margin-top:0">1FLOX (30ML)</span>
    </div>
    <div class="flavor">Natural Peppermint Flavor</div>
  </div>

  <section class="panel panel--facts">
    <div class="facts">
      <div class="facts-row facts-head"><strong>Supplement Facts</strong>Serving size 1ml<br>Serving Per Container 30</div>
      <div class="facts-row facts-calories"><span>Calories 8</span><span>Calories from Fat 8</span></div>
      <div class="facts-row facts-fat"><span>Total Fat</span><span>1g %2</span></div>
      <div class="facts-row facts-extract"><span>Full Spectrum Hemp Extract</span><span>24.99mg</span></div>
      <div class="facts-row facts-other">Other Ingredients: Hemp seed oil, Grape Seed Oil, Peppermint and Stevia</div>
    </div>
    <p class="distributor">DISTRIBUTED FOR:<br>Greenvale Extracts, INC.<br>support@marbleleafhemp.com</p>
  </section>
</div>
</body>
</html>
```